Professional/modern business card design for construction company

We need a new business card design, double sided keeping it modern, sleek, professional and simple. We are an earthmoving business but do not want any pictures of machinery. I would like one side to have the logo and the other to have all the information, keeping with the colors in our logo. The business card will need to be able to be customised so we can use it for several different managers., we would also like to be able to use the design to apply it to other stationary ie. letterheads, notebooks etc. We do not really have a tag line but we could put on there that we specialise in - Agriculture, Civil Construction and Mining.

Contact Information for Business Card

Brolga Ridge Excavations Pty Ltd
ABN 58 402 937 615
82 Gumleaf Creek Road, Moree NSW 2400

Harold Benton
Managing Director
P 0418 639 204
E haroldbenton@brolgaridgeexc.com.au

Font styles to use
Serif
Sans Serif

Requirements
Nice to have
• I have attached some examples of ideas.
Should not have
• images of machinery

```html
<!DOCTYPE html>
<html lang="en">
<head>
<meta charset="utf-8">
<title>Brolga Ridge Excavations – Business Card</title>
<link href="https://fonts.googleapis.com/css2?family=Roboto+Condensed:wght@400;700&display=swap" rel="stylesheet">
<style>
  :root {
    --backdrop: #d9d9db;
    --card-white: #ffffff;
    --charcoal: #48484b;
    --brand-grey: #4e4e51;
    --orange: #e58a2c;
    --text-light: #f2f2f2;
    --text-soft: #dcdcdc;
  }
  * { margin: 0; padding: 0; box-sizing: border-box; }
  html, body {
    width: 1200px; height: 960px; overflow: hidden;
    background: var(--backdrop);
    font-family: "Roboto Condensed", Arial, sans-serif;
  }
  .stage {
    position: relative; width: 1200px; height: 960px;
    display: flex; justify-content: center; align-items: center; gap: 80px;
  }
  .card {
    position: relative; width: 340px; height: 560px;
    background: var(--card-white);
    overflow: hidden;
    box-shadow: 0 6px 18px rgba(0,0,0,0.18);
  }
  .card__shape { position: absolute; inset: 0; width: 100%; height: 100%; }
  .brand {
    position: absolute; left: 0; right: 0;
    display: flex; align-items: center; justify-content: center; gap: 12px;
  }
  .brand__mark { width: 22px; height: 22px; background: var(--orange); flex: none; }
  .brand__name {
    color: var(--brand-grey); font-weight: 700; font-size: 30px;
    line-height: 1.0; text-transform: uppercase; letter-spacing: 0.5px;
  }
  .brand--front { top: 178px; }
  .brand--back { top: 70px; }
  .info {
    position: absolute; left: 0; right: 0; text-align: center;
    color: var(--text-light);
  }
  .info--company { top: 432px; }
  .company-name { font-weight: 700; font-size: 17px; margin-bottom: 4px; }
  .company-line { font-size: 15px; color: var(--text-soft); line-height: 1.35; }
  .sectors {
    margin-top: 16px; font-size: 14px; font-weight: 700; color: var(--orange);
    letter-spacing: 0.3px;
  }
  .sectors .divider { color: var(--text-light); font-weight: 400; margin: 0 5px; }
  .info--person { top: 300px; }
  .person-name { font-weight: 700; font-size: 20px; letter-spacing: 0.5px; text-transform: uppercase; }
  .person-title { font-size: 14px; color: var(--text-soft); margin-top: 2px; }
  .contact-icons { display: flex; justify-content: center; gap: 6px; margin: 20px 0 12px; }
  .contact-icons svg { width: 18px; height: 18px; }
  .contact-line { font-size: 14px; color: var(--text-soft); line-height: 1.5; }
  .website { margin-top: 16px; font-size: 15px; font-weight: 700; }
  .website .accent { color: var(--orange); text-transform: uppercase; }
</style>
</head>
<body>
<main class="stage">

  <section class="card card--front" aria-label="Business card front">
    <svg class="card__shape" viewBox="0 0 340 560" preserveAspectRatio="none" aria-hidden="true">
      <path d="M0,365 C70,430 230,430 340,335 L340,356 C235,440 85,445 0,380 Z" fill="var(--orange)"/>
      <path d="M0,392 C90,450 250,445 340,372 L340,560 L0,560 Z" fill="var(--charcoal)"/>
    </svg>
    <div class="brand brand--front">
      <span class="brand__mark"></span>
      <span class="brand__name">Brolga Ridge<br>Excavations</span>
    </div>
    <div class="info info--company">
      <p class="company-name">Brolga Ridge Excavations Pty Ltd</p>
      <p class="company-line">ABN 58 402 937 615</p>
      <p class="company-line">82 Gumleaf Creek Road, Moree NSW 2400</p>
      <p class="sectors">AGRICULTURE<span class="divider">|</span>CIVIL CONSTRUCTION<span class="divider">|</span>MINING</p>
    </div>
  </section>

  <section class="card card--back" aria-label="Business card back">
    <svg class="card__shape" viewBox="0 0 340 560" preserveAspectRatio="none" aria-hidden="true">
      <path d="M0,225 C80,290 235,285 340,185 L340,210 C240,298 85,305 0,240 Z" fill="var(--orange)"/>
      <path d="M0,252 C90,310 250,305 340,228 L340,560 L0,560 Z" fill="var(--charcoal)"/>
    </svg>
    <div class="brand brand--back">
      <span class="brand__mark"></span>
      <span class="brand__name">Brolga Ridge<br>Excavations</span>
    </div>
    <div class="info info--person">
      <p class="person-name">Harold Benton</p>
      <p class="person-title">Managing Director</p>
      <div class="contact-icons">
        <svg viewBox="0 0 20 20" aria-label="Phone">
          <circle cx="10" cy="10" r="10" fill="var(--orange)"/>
          <path d="M7 5.5 L8.6 5.2 L9.4 7.6 L8.3 8.5 C8.9 9.8 10 10.9 11.4 11.6 L12.3 10.5 L14.6 11.3 L14.4 12.9 C14.2 13.6 13.5 14 12.8 13.9 C9.4 13.3 6.6 10.5 6.1 7.1 C6 6.4 6.4 5.7 7 5.5 Z" fill="#fff"/>
        </svg>
        <svg viewBox="0 0 20 20" aria-label="Email">
          <circle cx="10" cy="10" r="10" fill="var(--orange)"/>
          <rect x="5" y="6.5" width="10" height="7" fill="#fff"/>
          <path d="M5 6.5 L10 10.5 L15 6.5" fill="none" stroke="var(--orange)" stroke-width="1"/>
        </svg>
      </div>
      <p class="contact-line">0418 639 204</p>
      <p class="contact-line">haroldbenton@brolgaridgeexc.com.au</p>
      <p class="website">www.<span class="accent">brolgaridgeexc</span>.com.au</p>
    </div>
  </section>

</main>
</body>
</html>
```